Business Card design for Recruiter providing Recruitment Staff Augmentation services

I need a double sided business card. I have used Zek to print cards in the past and really like their quality. I have a logo but need to change the tagline that is part of the graphic.

The tagline currently reads and Connnecting people with careers - but it should be removed.

The back should look like a notecard for writing a to do list with the first to-do Augment Recruiting Staff

```html
<!DOCTYPE html>
<html lang="en">
<head>
<meta charset="utf-8">
<title>Talent Peak – Business Card</title>
<link rel="stylesheet" href="https://fonts.googleapis.com/css2?family=Open+Sans:wght@400;600;700&display=swap">
<style>
  :root {
    --navy: #0b4263;
    --rust: #c4462b;
    --paper: #ffffff;
    --rule: #a8a8a8;
    --grey-text: #6a6a6a;
    --backdrop: #e6e6e6;
  }
  * { margin: 0; padding: 0; box-sizing: border-box; }
  html, body {
    width: 1105px; height: 1200px; overflow: hidden;
    background: var(--backdrop);
    font-family: "Open Sans", Arial, sans-serif;
  }
  .card {
    position: absolute; left: 192px; width: 720px; height: 412px;
    background: var(--paper); overflow: hidden;
  }
  .card--front { top: 166px; }
  .card--back { top: 622px; }
  .card-art { position: absolute; inset: 0; width: 720px; height: 412px; }

  .brand { position: absolute; left: 40px; top: 58px; display: flex; align-items: center; gap: 14px; }
  .brand-dot { width: 30px; height: 30px; border-radius: 50%; background: var(--rust); }
  .brand-name { font-size: 34px; font-weight: 600; color: var(--navy); letter-spacing: 1px; line-height: 1; }

  .person { position: absolute; left: 52px; top: 308px; }
  .person-name { font-size: 24px; font-weight: 700; color: var(--navy); line-height: 30px; }
  .person-role { font-size: 18px; font-weight: 400; color: var(--rust); line-height: 26px; }

  .contact { position: absolute; right: 43px; top: 182px; color: #fff; text-align: right; font-size: 18px; line-height: 28px; }
  .contact-address { margin-bottom: 4px; }
  .contact-row { display: flex; justify-content: flex-end; align-items: center; gap: 10px; height: 27.5px; }
  .contact-row svg { width: 18px; height: 18px; flex: none; }

  .back-brand-dot { position: absolute; left: 41px; top: 43px; width: 26px; height: 26px; border-radius: 50%; background: var(--rust); }
  .note-line { position: absolute; height: 1.5px; background: var(--rule); }
  .back-web { position: absolute; right: 59px; top: 331px; font-size: 18px; color: var(--grey-text); line-height: 26px; }
</style>
</head>
<body>

<section class="card card--front">
  <svg class="card-art" viewBox="0 0 521 298" preserveAspectRatio="none" aria-hidden="true">
    <circle cx="410" cy="238" r="164" fill="var(--rust)"/>
    <circle cx="413" cy="238" r="160" fill="var(--paper)"/>
    <circle cx="415" cy="239" r="157" fill="var(--navy)"/>
  </svg>

  <div class="brand">
    <span class="brand-dot"></span>
    <span class="brand-name">TALENT PEAK</span>
  </div>

  <div class="person">
    <p class="person-name">DANA HOLLIS</p>
    <p class="person-role">CEO/FOUNDER</p>
  </div>

  <div class="contact">
    <div class="contact-address">
      <p>2140 Birchwood Court</p>
      <p>Fairview, Oregon 97024</p>
    </div>
    <div class="contact-row"><span>503 214 7781</span>
      <svg viewBox="0 0 24 24" aria-label="phone"><path fill="#fff" d="M6.6 10.8a15.1 15.1 0 0 0 6.6 6.6l2.2-2.2c.3-.3.7-.4 1-.2 1.1.4 2.3.6 3.6.6.6 0 1 .4 1 1V20c0 .6-.4 1-1 1C10.6 21 3 13.4 3 4c0-.6.4-1 1-1h3.5c.6 0 1 .4 1 1 0 1.3.2 2.5.6 3.6.1.3 0 .7-.2 1z"/></svg>
    </div>
    <div class="contact-row"><span>503 868 1290</span>
      <svg viewBox="0 0 24 24" aria-label="mobile"><rect x="6" y="2" width="12" height="20" rx="2" fill="none" stroke="#fff" stroke-width="2"/><circle cx="12" cy="18.5" r="1.2" fill="#fff"/></svg>
    </div>
    <div class="contact-row"><span>503 214 7790</span>
      <svg viewBox="0 0 24 24" aria-label="fax"><rect x="6" y="3" width="12" height="6" fill="#fff"/><rect x="2" y="9" width="20" height="9" rx="1.5" fill="#fff"/><rect x="6" y="15" width="12" height="6" fill="#fff" stroke="var(--navy)" stroke-width="1.2"/></svg>
    </div>
    <div class="contact-row"><span>hello@talentpeak.co</span>
      <svg viewBox="0 0 24 24" aria-label="email"><rect x="2" y="5" width="20" height="14" fill="#fff"/><path d="M2 5l10 8 10-8" fill="none" stroke="var(--navy)" stroke-width="1.5"/></svg>
    </div>
    <div class="contact-row"><span>www.talentpeak.co</span>
      <svg viewBox="0 0 24 24" aria-label="website"><circle cx="12" cy="12" r="10" fill="#fff"/><path d="M7 8c2 0 3 1 3 3s-2 2-2 4M14 5c0 2 2 3 4 3M15 14c1 1 1 3 0 5" fill="none" stroke="var(--navy)" stroke-width="1.6"/></svg>
    </div>
  </div>
</section>

<section class="card card--back">
  <span class="back-brand-dot"></span>
  <div class="note-line" style="left:86px; width:575px; top:73px;"></div>
  <div class="note-line" style="left:47px; width:614px; top:129px;"></div>
  <div class="note-line" style="left:47px; width:614px; top:184px;"></div>
  <div class="note-line" style="left:47px; width:614px; top:238px;"></div>
  <div class="note-line" style="left:47px; width:614px; top:293px;"></div>
  <div class="note-line" style="left:47px; width:426px; top:348px;"></div>
  <p class="back-web">www.talentpeak.co</p>
</section>

</body>
</html>
```